WardPeak landing page

The existing website at www.wardpeak-example.com needs updating. I've attached some marketing material for the color scheme to be used and potential content. The tagline should be "Real-Time Operational Intelligence." I want the landing page to be in 3 categories in this order and features within each category. Plenty of images are preferred and wording can be modified.
Wardpeak Command Centre
- Live Incident tracking and reporting with escalation on critical incidents if necessary
- Geofence Monitoring to ensure guards at the right location at the right time.
- Smart scheduling to ensure the correct training and certifications are assigned to the appropriate guard required.
- Camera compatibility to capture live and historical video for incident reporting
WardPeak Back Office Administration
- Automate Police report filing using data from submitted incidents when required.
- Track all required KPIs on a per site basis such as vehicle inspections, patrol tour details, etc
- Payroll and Invoicing using smart shift reports
- Create and manage client sites with configurable geofencing
WardPeak App
- Guard can see all site details and instructions when logging onto shift
- Ability to view all incidents that have occured at that particular site over the last 'x' days. Understand what has been happening and when.
- Report incidents with all relevant information including photo and video
- Recieve alerts when repeat offences are occuring within a configurable vicinity.

Target Market(s)

Retailers and guard companies

Coding

Coded - Design and coding required

Number of Pages Required

1 page

Requirements
Nice to have
• Use the look and feel of the logo in the design

```html
<!DOCTYPE html>
<html lang="en">
<head>
<meta charset="utf-8">
<title>WardPeak – Real-Time Operational Intelligence</title>
<link href="https://fonts.googleapis.com/css2?family=Roboto+Condensed:wght@700;800&family=Inter:wght@400;500;600;700&display=swap" rel="stylesheet">
<style>
:root{
  --navy:#0f2747;
  --navy-deep:#0a1a33;
  --navy-card:#193660;
  --blue:#1a8fd6;
  --blue-bright:#1596d8;
  --grey-head:#8e97a3;
  --grey-bg:#f1f3f5;
  --text:#1b2533;
  --muted:#5d6673;
  --white:#ffffff;
}
*{box-sizing:border-box;margin:0;padding:0}
html,body{width:1200px;height:3222px;overflow:hidden}
body{font-family:"Inter",sans-serif;color:var(--text);background:var(--white);position:relative}
.display{font-family:"Roboto Condensed",sans-serif;font-weight:800;letter-spacing:-.3px}

/* Hero */
.hero{position:absolute;left:0;top:0;width:1200px;height:607px;overflow:hidden}
.hero-photo{position:absolute;inset:0;background:
  radial-gradient(ellipse at 70% 35%,rgba(40,110,160,.55),transparent 60%),
  radial-gradient(ellipse at 90% 90%,rgba(20,70,120,.6),transparent 55%),
  linear-gradient(100deg,#0b1e36 0%,#11304f 45%,#173f63 75%,#0c2744 100%)}
.brand{position:absolute;left:125px;top:52px;display:flex;align-items:center;gap:10px;color:var(--white);font-family:"Inter",sans-serif;font-weight:700;font-size:22px}
.brand .mark{width:18px;height:18px;background:var(--blue)}
.nav{position:absolute;left:616px;top:43px;width:466px;height:47px;background:var(--white);display:flex;align-items:center;padding:0 10px 0 24px;font-size:11px;color:var(--text)}
.nav a{color:inherit;text-decoration:none;margin-right:38px}
.nav a.active::before{content:"";display:inline-block;width:4px;height:4px;background:var(--blue);margin-right:6px;vertical-align:middle}
.login{margin-left:auto;background:var(--blue);color:var(--white);width:94px;height:32px;display:flex;align-items:center;justify-content:center;gap:6px;font-family:"Roboto Condensed",sans-serif;font-weight:700;font-size:11px}
.hero-copy{position:absolute;left:125px;top:222px;color:var(--white)}
.hero-copy .kicker{color:var(--blue);font-size:37px;line-height:1}
.hero-copy h1{font-size:62px;line-height:1;margin-top:6px}
.hero-copy .lead{font-size:15px;line-height:1.3;width:340px;margin-top:14px}
.hero-copy .small{font-size:9.5px;line-height:1.55;width:330px;margin-top:14px}
.btn{display:inline-flex;align-items:center;justify-content:center;font-family:"Roboto Condensed",sans-serif;font-weight:700;font-size:11px;text-transform:uppercase;text-decoration:none}
.btn-primary{background:var(--blue);color:var(--white);width:141px;height:32px;margin-top:16px}

/* Trust */
.trust{position:absolute;left:0;top:607px;width:1200px;height:380px;background:var(--white)}
.trust-mark{position:absolute;left:125px;top:160px;display:flex;align-items:center;gap:10px;font-weight:700;font-size:30px;color:var(--navy)}
.trust-mark .mark{width:24px;height:24px;background:var(--blue)}
.trust h2{position:absolute;left:352px;top:128px;font-size:40px;line-height:1;color:var(--navy);width:600px}
.trust h2 span{color:var(--grey-head)}

/* Feature sections */
.features{position:absolute;left:0;width:1200px}
.features h2{position:absolute;left:125px;font-size:36px;line-height:1}
.features .intro{position:absolute;left:125px;width:620px;font-size:9.5px;line-height:1.55;color:var(--muted)}
.cards{position:absolute;left:125px;display:flex;gap:16px}
.card{width:225px;height:244px;padding:26px 24px 0 26px}
.check{width:22px;height:22px;background:var(--blue);display:flex;align-items:center;justify-content:center}
.card h3{font-family:"Roboto Condensed",sans-serif;font-weight:700;font-size:17px;line-height:1.15;margin-top:25px;min-height:20px}
.card ul{list-style:none;margin-top:10px}
.card li{font-size:9px;line-height:1.5;color:var(--muted);padding-left:9px;position:relative;margin-bottom:9px}
.card li::before{content:"";position:absolute;left:0;top:4px;width:4px;height:4px;background:var(--blue)}

.command{top:987px;height:479px;background:var(--grey-bg)}
.command h2{top:63px;color:var(--navy)}
.command .intro{top:108px}
.command .cards{top:171px}
.command .card{background:var(--white)}
.command h3{color:var(--navy)}

.backoffice{top:1466px;height:513px;background:var(--white)}
.backoffice h2{top:77px;color:var(--navy)}
.backoffice .intro{top:125px}
.backoffice .cards{top:189px}
.backoffice .card{background:var(--grey-bg)}
.backoffice h3{color:var(--navy)}

.app{top:1979px;height:480px;background:var(--navy)}
.app h2{top:59px;color:var(--white)}
.app .intro{top:108px;color:#c9d3df}
.app .cards{top:173px}
.app .card{background:var(--navy-card)}
.app h3{color:var(--white)}
.app .card li{color:#c3cedb}

/* CTA */
.cta{position:absolute;left:0;top:2459px;width:1200px;height:341px;display:flex}
.cta-photo{width:600px;height:341px;background:
  radial-gradient(ellipse at 45% 55%,#2a4a6e,transparent 60%),
  linear-gradient(135deg,#0c1c33 0%,#17375a 55%,#0d2240 100%)}
.cta-panel{width:600px;height:341px;background:var(--blue-bright);padding:67px 0 0 89px;color:var(--white)}
.cta-panel h2{font-size:37px;line-height:1.08;width:380px}
.cta-panel p{font-size:9.5px;line-height:1.55;width:350px;margin-top:14px}
.btn-light{background:var(--white);color:var(--navy);width:140px;height:33px;margin-top:17px}

/* Footer */
.footer{position:absolute;left:0;top:2800px;width:1200px;height:422px;background:
  radial-gradient(ellipse at 100% 0%,#b9dcef 0%,rgba(185,220,239,0) 45%),#f5f7f9;text-align:center}
.footer-brand{position:absolute;left:0;right:0;top:150px;display:flex;justify-content:center;align-items:center;gap:12px;font-weight:700;font-size:34px;color:var(--navy)}
.footer-brand .mark{width:22px;height:22px;background:var(--blue)}
.footer-desc{position:absolute;left:410px;width:380px;top:229px;font-size:9.5px;line-height:1.55;color:var(--muted)}
.socials{position:absolute;left:550px;top:276px;display:flex;gap:8px}
.socials span{width:28px;height:28px;background:var(--blue);display:block}
.footer-rule{position:absolute;left:125px;right:125px;top:384px;border-top:1px solid #d7dce2}
.footer-bottom{position:absolute;left:125px;right:125px;top:395px;display:flex;justify-content:space-between;font-size:9.5px;color:var(--muted)}
</style>
</head>
<body>

<header class="hero">
  <div class="hero-photo" role="img" aria-label="Dark security operations centre with operators at monitoring screens"></div>
  <div class="brand"><span class="mark"></span>WardPeak</div>
  <nav class="nav">
    <a href="#" class="active">Home</a>
    <a href="#">Features</a>
    <a href="#">Pricing</a>
    <a href="#">Contact Us</a>
    <a href="#" class="login">
      <svg width="10" height="10" viewBox="0 0 10 10" fill="none" stroke="#fff" stroke-width="1"><circle cx="5" cy="3" r="2"/><path d="M1 9.5c0-2.2 1.8-3.5 4-3.5s4 1.3 4 3.5"/></svg>
      LOGIN
    </a>
  </nav>
  <div class="hero-copy">
    <div class="kicker display">Real-Time Operational</div>
    <h1 class="display">Intelligence</h1>
    <p class="lead">Manage your entire security workforce within one secure platform</p>
    <p class="small">Streamline operations, enhance security, and ensure compliance with WardPeak's integrated management solution.</p>
    <a href="#" class="btn btn-primary">Request a Demo</a>
  </div>
</header>

<section class="trust">
  <div class="trust-mark"><span class="mark"></span>WardPeak</div>
  <h2 class="display">Trusted By Security Teams To Deliver Real-Time Visibility, <span>Compliance, And Accountability.</span></h2>
</section>

<section class="features command">
  <h2 class="display">Wardpeak Command Centre</h2>
  <p class="intro">Centralized Command. Immediate Insight. Description: The WardPeak Command Centre provides live visibility into every incident, guard movement, and site condition—empowering supervisors to act decisively.</p>
  <div class="cards">
    <article class="card"><div class="check"><svg width="12" height="10" viewBox="0 0 12 10"><path d="M1 5l3.5 3.5L11 1.5" fill="none" stroke="#fff" stroke-width="2"/></svg></div>
      <h3>Live Incident Tracking &amp; Escalation</h3>
      <ul><li>Real-time incident tracking with detailed reporting</li><li>Automated escalation workflows for critical incidents</li><li>Supervisor visibility across all active sites</li></ul></article>
    <article class="card"><div class="check"><svg width="12" height="10" viewBox="0 0 12 10"><path d="M1 5l3.5 3.5L11 1.5" fill="none" stroke="#fff" stroke-width="2"/></svg></div>
      <h3>Geofence Monitoring</h3>
      <ul><li>Ensure guards are at the right location at the right time</li><li>Real-time entry and exit validation</li><li>Reduce missed patrols and unauthorized movement</li></ul></article>
    <article class="card"><div class="check"><svg width="12" height="10" viewBox="0 0 12 10"><path d="M1 5l3.5 3.5L11 1.5" fill="none" stroke="#fff" stroke-width="2"/></svg></div>
      <h3>Smart Scheduling &amp; Certifications</h3>
      <ul><li>Automatically assign guards based on required training and certifications</li><li>Reduce compliance risk and manual scheduling errors</li><li>Optimize coverage across all sites</li></ul></article>
    <article class="card"><div class="check"><svg width="12" height="10" viewBox="0 0 12 10"><path d="M1 5l3.5 3.5L11 1.5" fill="none" stroke="#fff" stroke-width="2"/></svg></div>
      <h3>Camera Compatibility</h3>
      <ul><li>Integrate with compatible camera systems</li><li>Capture live and historical video for incident reporting</li><li>Strengthen evidence and accountability</li></ul></article>
  </div>
</section>

<section class="features backoffice">
  <h2 class="display">WardPeak Back Office Administration</h2>
  <p class="intro">Automate Administration. Gain Total Oversight. Description: WardPeak's back office tools reduce paperwork, improve accuracy, and provide actionable insights across every client site.</p>
  <div class="cards">
    <article class="card"><div class="check"><svg width="12" height="10" viewBox="0 0 12 10"><path d="M1 5l3.5 3.5L11 1.5" fill="none" stroke="#fff" stroke-width="2"/></svg></div>
      <h3>Automated Police Report Filing</h3>
      <ul><li>Generate police reports directly from incident data</li><li>Reduce manual data entry and reporting delays</li><li>Ensure accuracy and consistency</li></ul></article>
    <article class="card"><div class="check"><svg width="12" height="10" viewBox="0 0 12 10"><path d="M1 5l3.5 3.5L11 1.5" fill="none" stroke="#fff" stroke-width="2"/></svg></div>
      <h3>KPI Tracking By Site</h3>
      <ul><li>Track KPIs such as patrol tours, vehicle inspections, and site activity</li><li>Site-by-site performance visibility</li><li>Data-driven operational improvements</li></ul></article>
    <article class="card"><div class="check"><svg width="12" height="10" viewBox="0 0 12 10"><path d="M1 5l3.5 3.5L11 1.5" fill="none" stroke="#fff" stroke-width="2"/></svg></div>
      <h3>Payroll &amp; Invoicing</h3>
      <ul><li>Automated payroll using smart shift reports</li><li>Accurate invoicing tied directly to completed work</li><li>Reduce disputes and administrative overhead</li></ul></article>
    <article class="card"><div class="check"><svg width="12" height="10" viewBox="0 0 12 10"><path d="M1 5l3.5 3.5L11 1.5" fill="none" stroke="#fff" stroke-width="2"/></svg></div>
      <h3>Site &amp; Geofence Management</h3>
      <ul><li>Create and manage multiple client sites</li><li>Configure site-specific geofencing rules</li><li>Scale operations with ease</li></ul></article>
  </div>
</section>

<section class="features app">
  <h2 class="display">WardPeak App</h2>
  <p class="intro">Everything Guards Need. Right in Their Hands. Description: The WardPeak mobile app ensures guards are informed, connected, and equipped to respond effectively.</p>
  <div class="cards">
    <article class="card"><div class="check"><svg width="12" height="10" viewBox="0 0 12 10"><path d="M1 5l3.5 3.5L11 1.5" fill="none" stroke="#fff" stroke-width="2"/></svg></div>
      <h3>Site Details &amp; Shift Instructions</h3>
      <ul><li>Guards view site instructions upon logging into a shift</li><li>Clear expectations and procedures</li><li>Reduced onboarding and training friction</li></ul></article>
    <article class="card"><div class="check"><svg width="12" height="10" viewBox="0 0 12 10"><path d="M1 5l3.5 3.5L11 1.5" fill="none" stroke="#fff" stroke-width="2"/></svg></div>
      <h3>Incident History Visibility</h3>
      <ul><li>View incidents from the past configurable number of days</li><li>Understand recurring issues and site patterns</li><li>Improve situational awareness</li></ul></article>
    <article class="card"><div class="check"><svg width="12" height="10" viewBox="0 0 12 10"><path d="M1 5l3.5 3.5L11 1.5" fill="none" stroke="#fff" stroke-width="2"/></svg></div>
      <h3>Incident Reporting With Media</h3>
      <ul><li>Report incidents with structured forms</li><li>Attach photos and videos directly from the app</li><li>Improve report quality and response times</li></ul></article>
    <article class="card"><div class="check"><svg width="12" height="10" viewBox="0 0 12 10"><path d="M1 5l3.5 3.5L11 1.5" fill="none" stroke="#fff" stroke-width="2"/></svg></div>
      <h3>Repeat Offence Alerts</h3>
      <ul><li>Receive alerts for repeat offences within a configurable vicinity</li><li>Proactive awareness and faster response</li><li>Enhanced site security intelligence</li></ul></article>
  </div>
</section>

<section class="cta">
  <div class="cta-photo" role="img" aria-label="Security team standing in front of a monitoring wall in a control room"></div>
  <div class="cta-panel">
    <h2 class="display">See Real-Time Operational Intelligence In Action</h2>
    <p>Discover how WardPeak transforms security operations from the field to the command center.</p>
    <a href="#" class="btn btn-light">Request a Demo</a>
  </div>
</section>

<footer class="footer">
  <div class="footer-brand"><span class="mark"></span>WardPeak</div>
  <p class="footer-desc">Real-time operational intelligence for modern security operations. Empowering security teams with visibility, control, and accountability.</p>
  <div class="socials" aria-label="Social links"><span></span><span></span><span></span></div>
  <div class="footer-rule"></div>
  <div class="footer-bottom"><span>© 2026 WardPeak. All rights reserved.</span><span>Privacy Policy | Terms of Service</span></div>
</footer>

</body>
</html>
```